Redesign my business cards

I would like pretty much all the same information as my current business cards but redesigned to stand out more and be more unique photo uploaded to show my current business cards don’t mind if you want to remove or replace I for on the back

```html
<!DOCTYPE html>
<html lang="en">
<head>
<meta charset="utf-8">
<title>Harbourline Detailing – Business Cards</title>
<link href="https://fonts.googleapis.com/css2?family=Lato:wght@400;700;900&display=swap" rel="stylesheet">
<style>
  :root {
    --backdrop: #b5b5b5;
    --card-white: #ffffff;
    --navy: #2b2f7a;
    --magenta: #b3509b;
    --sky: #1690c6;
    --name-blue: #1a86bf;
    --text-grey: #6a6a6a;
    --rule-grey: #c9c9c9;
  }
  * { margin: 0; padding: 0; box-sizing: border-box; }
  html, body { width: 1200px; height: 900px; overflow: hidden; }
  body {
    background: var(--backdrop);
    font-family: "Lato", sans-serif;
    position: relative;
  }
  .card {
    position: absolute;
    left: 363px;
    width: 475px;
    height: 271px;
    overflow: hidden;
  }
  .card--front { top: 145px; background: var(--card-white); }
  .card--back { top: 484px; }

  /* Front */
  .brand-mark {
    position: absolute;
    left: 80px; top: 74px;
    width: 120px; height: 120px;
    border-radius: 50%;
    background: radial-gradient(circle at 50% 45%, #e8f3fa 0 52%, #cfe6f4 53% 100%);
    border: 3px solid var(--name-blue);
    display: flex; align-items: center; justify-content: center;
    text-align: center;
  }
  .brand-mark__name {
    font-weight: 900;
    font-size: 13px;
    line-height: 1.25;
    letter-spacing: 1px;
    color: var(--navy);
    text-transform: uppercase;
  }
  .divider {
    position: absolute;
    left: 229px; top: 81px;
    width: 1px; height: 108px;
    background: var(--rule-grey);
  }
  .contact { position: absolute; left: 261px; top: 93px; }
  .contact__name {
    font-weight: 700; font-size: 16px;
    color: var(--name-blue);
    letter-spacing: 0.2px;
  }
  .contact__role { font-size: 12px; color: var(--text-grey); margin-top: 1px; }
  .contact__list { list-style: none; margin-top: 20px; }
  .contact__item {
    display: flex; align-items: center; gap: 6px;
    font-size: 11.5px; color: var(--text-grey); line-height: 14px;
  }
  .contact__icon { width: 9px; height: 9px; flex: none; }
  .stripe {
    position: absolute; top: 233px; height: 22px;
  }
  .stripe--navy { left: 0; width: 378px; background: var(--navy); }
  .stripe--magenta { left: 378px; right: 0; background: var(--magenta); }
  .stripe-dot {
    position: absolute; left: 360px; top: 227px;
    width: 34px; height: 34px; border-radius: 50%;
    background: var(--card-white);
    border: 3px solid var(--navy);
  }

  /* Back */
  .service {
    position: absolute; left: 0; right: 0;
  }
  .service--interior { top: 0; height: 101px; background: var(--navy); }
  .service--exterior { top: 101px; height: 77px; background: var(--magenta); }
  .service--full { top: 178px; height: 93px; background: var(--sky); }
  .service__price {
    position: absolute; right: 270px;
    font-weight: 700; font-size: 22px; color: #fff;
  }
  .service__info { position: absolute; left: 221px; right: 28px; color: #fff; }
  .service__title { font-weight: 700; font-size: 13.5px; line-height: 16px; text-transform: uppercase; }
  .service__desc { font-size: 10.8px; line-height: 13.2px; }
  .service--interior .service__price { top: 43px; }
  .service--interior .service__info { top: 18px; }
  .service--exterior .service__price { top: 27px; }
  .service--exterior .service__info { top: 8px; }
  .service--full .service__price { top: 34px; }
  .service__info--full { top: 2px; }
  .back-emblem {
    position: absolute; left: 20px; top: 76px;
    width: 126px; height: 126px; border-radius: 50%;
    background: radial-gradient(circle at 45% 40%, #8aa3e6, #4a3fa0 70%);
    border: 3px solid #ffffff;
    display: flex; align-items: center; justify-content: center;
    text-align: center;
  }
  .back-emblem__name {
    font-weight: 900; font-size: 13px; line-height: 1.25;
    letter-spacing: 1px; color: #fff; text-transform: uppercase;
  }
</style>
</head>
<body>

<section class="card card--front" aria-label="Business card front">
  <div class="brand-mark">
    <span class="brand-mark__name">Harbourline<br>Detailing</span>
  </div>
  <div class="divider"></div>
  <div class="contact">
    <h1 class="contact__name">DANE MORROW</h1>
    <p class="contact__role">Owner/Operator</p>
    <ul class="contact__list">
      <li class="contact__item">
        <svg class="contact__icon" viewBox="0 0 10 10" aria-hidden="true"><path d="M2 1 L4 1 L4.6 3 L3.4 3.8 Q4.4 5.8 6.2 6.6 L7 5.4 L9 6 L9 8 Q5 9 2.5 6.5 Q1 4.5 2 1Z" fill="var(--name-blue)"/></svg>
        <span>0412 555 017</span>
      </li>
      <li class="contact__item">
        <svg class="contact__icon" viewBox="0 0 10 10" aria-hidden="true"><rect x="0.5" y="2" width="9" height="6" fill="var(--name-blue)"/><path d="M0.5 2 L5 5.5 L9.5 2" stroke="#fff" stroke-width="0.9" fill="none"/></svg>
        <span>bookings@harbourlinedetailing.com.au</span>
      </li>
    </ul>
  </div>
  <div class="stripe stripe--navy"></div>
  <div class="stripe stripe--magenta"></div>
  <div class="stripe-dot"></div>
</section>

<section class="card card--back" aria-label="Business card back, service prices">
  <div class="service service--interior">
    <p class="service__price">$150</p>
    <div class="service__info">
      <h2 class="service__title">Interior Detail</h2>
      <p class="service__desc">Vacume &amp; deep clean of carpets&nbsp; upholstery or leather treatment, interiro trim clean condition. Windows polish and treatment, steam clean and stain removal.</p>
    </div>
  </div>
  <div class="service service--exterior">
    <p class="service__price">$250</p>
    <div class="service__info">
      <h2 class="service__title">Exterior Detail</h2>
      <p class="service__desc">Extreme wash &amp; polish, exterior trim reviver &amp; protector windows. Polish &amp; treatment, tyre dressing, engine bay cleaned</p>
    </div>
  </div>
  <div class="service service--full">
    <p class="service__price">$350</p>
    <div class="service__info service__info--full">
      <h2 class="service__title">Full Extremedetail</h2>
      <p class="service__desc">Extreme wash &amp; polish, tyre dressing, engine bay cleaned, vacume &amp; deep clean of carpets upholstery or leather treatment, interior &amp; exterior trim reviver &amp; protector, window polish and treatment</p>
    </div>
  </div>
  <div class="back-emblem">
    <span class="back-emblem__name">Harbourline<br>Detailing</span>
  </div>
</section>

</body>
</html>
```